Brochure for a paper wholesaler who wants to educate his print industry clients

We will be making a stapled informative brochure, that contains basic information about our paper products - the types of paper there is, their characteristics and other useful information.
As we are part of a paper wholesaler group in Europe - VORENT, we received a brochure in German that has this kind of information. The text in it is not as important. What is important is the layout of the document and how the text will appear in it (added in the uploaded files - 210915_Wiessenswertes_TBLK_F51.pdf).
We are allowed to tinker with this file and adjust it to our needs. So there are also .idml and .indd files available (also in the uploaded files).
We would like to keep the custom page size of 210 x290mm (8.3x11.4 in), or you can go up to 210x297mm (8.3x11.7 in).
What we want is a modern looking design that contains our companies red bordo and white/ grey colours to replace the existing green colours in this borchure. The pictures and appearance of the file can be changed according to your views and what you think would look good. We don't necessarily want to keep the same design, we just want the layout of the document be the same, as we will be placing our translated text into it. The VORENT logo should be replaced with our own logo (KUMET Logo.png).
As for how it could look, it could go together with our paper presentation, for which the design can be seen in the "KUMET Base - v2.pptx".
Holiday season, so have a lot of tasks to take care of and not as much time to check ArtHarbor as often.

```html
<!DOCTYPE html>
<html lang="en">
<head>
<meta charset="utf-8">
<title>KUMET – Brochure Cover</title>
<link href="https://fonts.googleapis.com/css2?family=Poppins:wght@400;500;800&display=swap" rel="stylesheet">
<style>
  :root {
    --backdrop: #0f0f0f;
    --paper: #ffffff;
    --bordo: #8b2f33;
    --band-grey: #f3f3f3;
    --ink: #0a0a0a;
    --press-light: #d9d9d9;
    --press-mid: #8e8e8e;
    --press-dark: #2e2e2e;
  }
  html, body {
    margin: 0;
    padding: 0;
    width: 1200px;
    height: 1200px;
    overflow: hidden;
    background: var(--backdrop);
    font-family: "Poppins", Arial, sans-serif;
  }
  .cover {
    position: absolute;
    left: 244px;
    top: 96px;
    width: 714px;
    height: 985px;
    background: var(--paper);
    overflow: hidden;
  }
  .cover__graphics {
    position: absolute;
    inset: 0;
    width: 100%;
    height: 100%;
  }
  .accent { fill: var(--bordo); }
  .title-band {
    position: absolute;
    left: 34px;
    top: 370px;
    width: 646px;
    height: 81px;
    background: var(--band-grey);
  }
  .brand {
    position: absolute;
    left: 0;
    right: 0;
    top: 200px;
    text-align: center;
  }
  .brand__mark {
    display: block;
    width: 58px;
    height: 58px;
    margin: 0 auto;
    border: 4px solid var(--bordo);
    box-sizing: border-box;
  }
  .brand__name {
    margin: 40px 0 0;
    font-weight: 500;
    font-size: 34px;
    line-height: 1;
    letter-spacing: 30px;
    padding-left: 30px;
    color: var(--bordo);
  }
  .headline {
    position: absolute;
    left: 0;
    right: 0;
    top: 373px;
    margin: 0;
    text-align: center;
    font-weight: 400;
    font-size: 31px;
    line-height: 37px;
    color: var(--ink);
  }
  .headline strong { font-weight: 800; }
  .tagline {
    position: absolute;
    left: 0;
    right: 0;
    top: 464px;
    margin: 0;
    text-align: center;
    font-size: 15px;
    line-height: 22px;
    color: var(--ink);
  }
  .divider {
    position: absolute;
    left: 312px;
    top: 511px;
    width: 91px;
    height: 3px;
    background: var(--bordo);
  }
</style>
</head>
<body>
  <main class="cover">
    <svg class="cover__graphics" viewBox="0 0 1149 1586" preserveAspectRatio="none" aria-hidden="false">
      <defs>
        <linearGradient id="pressTones" x1="0" y1="0" x2="1" y2="1">
          <stop offset="0" stop-color="var(--press-mid)"/>
          <stop offset="0.35" stop-color="var(--press-light)"/>
          <stop offset="0.7" stop-color="#c9c9cc"/>
          <stop offset="1" stop-color="var(--press-dark)"/>
        </linearGradient>
      </defs>
      <rect class="press-photo" x="55" y="1290" width="1094" height="296" fill="url(#pressTones)" role="img" aria-label="Photo of a printing press running printed paper through its rollers"/>
      <polygon class="accent corner-chevron" points="7,0 50,0 195,147 350,0 356,0 175,171"/>
      <polygon class="accent side-bar side-bar--left" points="0,329 55,387 55,1586 0,1586"/>
      <polygon class="accent side-bar side-bar--right" points="1095,0 1149,0 1149,961 1095,918"/>
      <polygon class="accent corner-chevron" points="740,1290 954,1084 1149,1281 1149,1321 935,1110 746,1290"/>
    </svg>

    <div class="title-band"></div>

    <div class="brand">
      <span class="brand__mark"></span>
      <p class="brand__name">KUMET</p>
    </div>

    <h1 class="headline">WE HELP LATVIAN PRINTING<br>INDUSTRY <strong>GROW</strong></h1>
    <p class="tagline">Your growth is our priority!</p>
    <div class="divider"></div>
  </main>
</body>
</html>
```